Brennick Holdings Business Cards

These are professional business cards that are for my family office.
Put fake emails and phone numbers as of now until I finalize those components. This family office controls my families investments, assets, and future. The cards should be professional.
..
.
.
.
I just uploaded another variation of a logo I would like to see as a business card to I am inbeteen which logo to use

Target Market(s)

business

Industry/Entity Type

business

Contact Information for Business Card

Professional, wealth related, finance related.

Requirements
Must have
• Logo

```html
<!DOCTYPE html>
<html lang="en">
<head>
<meta charset="utf-8">
<title>Brennick Holdings — Business Cards</title>
<link rel="stylesheet" href="https://fonts.googleapis.com/css2?family=Cinzel:wght@600&family=Montserrat:wght@400;600;700&display=swap">
<style>
  :root {
    --ink: #2a2c38;
    --stone: #b1b0ab;
    --paper: #ffffff;
    --backdrop: #ffffff;
  }
  * { box-sizing: border-box; margin: 0; padding: 0; }
  html, body {
    width: 1200px; height: 1200px; overflow: hidden;
    background: var(--backdrop);
  }
  .sheet { position: relative; width: 1200px; height: 1200px; }
  .card {
    position: absolute; left: 181px; width: 845px; height: 483px;
    background: var(--paper);
    box-shadow: 0 0 40px rgba(0,0,0,0.22);
  }
  .card--front { top: 94px; }
  .card--back { top: 631px; }

  .brand { position: absolute; text-align: center; width: 360px; }
  .brand__ring { display: block; margin: 0 auto; }
  .brand__name {
    font-family: "Cinzel", serif; font-weight: 600;
    font-size: 26px; letter-spacing: 0.5px; color: var(--ink);
    white-space: nowrap; margin-top: 30px;
  }
  .card--front .brand { left: 244px; top: 137px; }
  .card--back .brand { left: 49px; top: 138px; }

  .front__web {
    position: absolute; right: 52px; top: 424px;
    font-family: "Montserrat", sans-serif; font-size: 20px;
    color: var(--ink); letter-spacing: 0.4px;
  }

  .person { position: absolute; left: 466px; top: 120px; font-family: "Montserrat", sans-serif; color: var(--ink); }
  .person__name { font-size: 31px; font-weight: 700; letter-spacing: 3.5px; line-height: 1; }
  .person__title { font-size: 18px; font-weight: 700; margin-top: 8px; letter-spacing: 0.4px; }

  .contacts { position: absolute; left: 466px; top: 208px; list-style: none; font-family: "Montserrat", sans-serif; }
  .contacts__item { display: flex; align-items: center; height: 30px; margin-bottom: 9.5px; }
  .contacts__icon { width: 30px; height: 30px; flex: none; }
  .contacts__text { margin-left: 19px; font-size: 19px; color: var(--ink); letter-spacing: 0.3px; }
  .contacts__text--phone { letter-spacing: 2.5px; }
</style>
</head>
<body>
<main class="sheet">

  <section class="card card--front">
    <div class="brand">
      <svg class="brand__ring" width="164" height="164" viewBox="0 0 164 164" aria-hidden="true">
        <circle cx="82" cy="82" r="78" fill="none" stroke="var(--ink)" stroke-width="3"/>
      </svg>
      <p class="brand__name">Brennick Holdings</p>
    </div>
    <p class="front__web">www.yourwebsite.com</p>
  </section>

  <section class="card card--back">
    <div class="brand">
      <svg class="brand__ring" width="164" height="164" viewBox="0 0 164 164" aria-hidden="true">
        <circle cx="82" cy="82" r="78" fill="none" stroke="var(--ink)" stroke-width="3"/>
      </svg>
      <p class="brand__name">Brennick Holdings</p>
    </div>

    <div class="person">
      <p class="person__name">Your Name</p>
      <p class="person__title">Your Title</p>
    </div>

    <ul class="contacts">
      <li class="contacts__item">
        <svg class="contacts__icon" viewBox="0 0 30 30" aria-hidden="true">
          <circle cx="15" cy="15" r="15" fill="var(--stone)"/>
          <path d="M10 8.5l2.6-.6 1.6 3.6-1.7 1.2c.8 1.8 2.1 3.1 3.9 3.9l1.2-1.7 3.6 1.6-.6 2.6c-.2.7-.8 1-1.5 1C13.3 19.8 10.2 16.7 9.9 10c0-.7.4-1.3 1-1.5z" fill="#fff"/>
        </svg>
        <span class="contacts__text contacts__text--phone">123-456-789</span>
      </li>
      <li class="contacts__item">
        <svg class="contacts__icon" viewBox="0 0 30 30" aria-hidden="true">
          <circle cx="15" cy="15" r="15" fill="var(--stone)"/>
          <g fill="none" stroke="#fff" stroke-width="1.1">
            <circle cx="15" cy="15" r="7"/>
            <ellipse cx="15" cy="15" rx="3" ry="7"/>
            <path d="M8 15h14M9 11.5h12M9 18.5h12"/>
          </g>
        </svg>
        <span class="contacts__text">www.yourwebsite.com</span>
      </li>
      <li class="contacts__item">
        <svg class="contacts__icon" viewBox="0 0 30 30" aria-hidden="true">
          <circle cx="15" cy="15" r="15" fill="var(--stone)"/>
          <rect x="8.5" y="10.5" width="13" height="9" fill="none" stroke="#fff" stroke-width="1.2"/>
          <path d="M8.5 10.5l6.5 5 6.5-5" fill="none" stroke="#fff" stroke-width="1.2"/>
        </svg>
        <span class="contacts__text">email@info.com</span>
      </li>
      <li class="contacts__item">
        <svg class="contacts__icon" viewBox="0 0 30 30" aria-hidden="true">
          <circle cx="15" cy="15" r="15" fill="var(--stone)"/>
          <path d="M15 24s-6-6.4-6-10.6a6 6 0 0 1 12 0C21 17.6 15 24 15 24z" fill="#fff"/>
          <circle cx="15" cy="13.5" r="2.2" fill="var(--stone)"/>
        </svg>
        <span class="contacts__text">Your Address and Country</span>
      </li>
    </ul>
  </section>

</main>
</body>
</html>
```